Contemporary Elegant Business Card Design for an International Trade Company in the Wine Industry

We need a new business card design for an international trade company in the wine and winemaking industry. The overall feel of the card should be contemporary, upscale, luxurious and elegant. It should communicate confidence and professionalism. The colors should complementary to our logo design (burgundy, gold, and black).
Inspiration: rich velvet tapestry
The card should include the following information:
Business: Brovenna Trading/Shipping, LLC.
Name: Marcus T. Hollenbrand
Title: CEO
Email: mark@brovennatrading.example
Phone: 555-294-6172
www.brovennatrading.example
Updates
Project Deadline Extended
Reason: We'd like the designers that we requested some additional designs from to still submit designs. Thank you!
Industry/Entity Type
Business
Contact Information for Business Card
Title: CEO
Phone: 555-294-6172
www.brovennatrading.example
Look and feel

```html
<!DOCTYPE html>
<html lang="en">
<head>
<meta charset="utf-8">
<title>Brovenna Trading/Shipping — Business Card</title>
<link rel="stylesheet" href="https://fonts.googleapis.com/css2?family=Montserrat:wght@400;500;600&display=swap">
<style>
  :root {
    --backdrop: #e4e5e8;
    --charcoal: #454547;
    --charcoal-light: #525254;
    --gold: #e8c06a;
    --gold-deep: #dba744;
    --silver: #c9cacc;
    --edge-white: #f4f4f4;
    --burgundy: #7a1c1c;
    --ink: #3a3a3a;
  }
  * { margin: 0; padding: 0; box-sizing: border-box; }
  html, body {
    width: 1200px;
    height: 1000px;
    overflow: hidden;
    background: var(--backdrop);
    font-family: "Montserrat", sans-serif;
  }
  .sheet {
    position: relative;
    width: 1200px;
    height: 1000px;
  }
  .card {
    position: absolute;
    left: 320px;
    width: 560px;
    height: 320px;
    box-shadow: 0 10px 28px rgba(0,0,0,0.16);
  }
  .card--front { top: 130px; }
  .card--back { top: 550px; }
  .card svg { display: block; width: 560px; height: 320px; }
  .brand-name { font-family: "Montserrat", sans-serif; font-weight: 600; letter-spacing: 0.06em; }
  .brand-sub { font-family: "Montserrat", sans-serif; font-weight: 600; letter-spacing: 0.08em; }
  .holder-name { font-family: "Montserrat", sans-serif; font-weight: 500; }
  .contact-line { font-family: "Montserrat", sans-serif; font-weight: 400; }
</style>
</head>
<body>
<main class="sheet">

  <!-- Front of card -->
  <section class="card card--front" aria-label="Card front">
    <svg viewBox="0 0 560 320" xmlns="http://www.w3.org/2000/svg">
      <rect class="card-base" width="560" height="320" fill="var(--charcoal)"/>
      <g class="world-map" role="img" aria-label="Faint globe with world map outline">
        <circle cx="450" cy="110" r="130" fill="var(--charcoal-light)" opacity="0.55"/>
      </g>
      <polygon class="chevron-edge" points="240,0 266,0 356,160 266,320 240,320 330,160" fill="var(--silver)"/>
      <polygon class="chevron-rule" points="240,0 246,0 336,160 246,320 240,320 330,160" fill="var(--edge-white)"/>
      <polygon class="gold-panel" points="0,0 240,0 330,160 240,320 0,320" fill="var(--gold)"/>
      <g class="brand-lockup">
        <rect x="40" y="128" width="30" height="30" fill="var(--burgundy)"/>
        <text class="brand-name" x="80" y="148" font-size="19" fill="var(--burgundy)">BROVENNA</text>
        <text class="brand-sub" x="40" y="180" font-size="9.5" fill="var(--burgundy)">TRADING/SHIPPING, LLC.</text>
      </g>
    </svg>
  </section>

  <!-- Back of card -->
  <section class="card card--back" aria-label="Card back">
    <svg viewBox="0 0 560 320" xmlns="http://www.w3.org/2000/svg">
      <rect class="card-base" width="560" height="320" fill="var(--charcoal)"/>
      <polygon class="chevron-edge" points="274,0 300,0 210,160 300,320 274,320 184,160" fill="var(--silver)"/>
      <polygon class="chevron-rule" points="294,0 300,0 210,160 300,320 294,320 204,160" fill="var(--edge-white)"/>
      <polygon class="gold-panel" points="300,0 560,0 560,320 300,320 210,160" fill="var(--gold)"/>
      <rect class="gold-stripe" x="516" y="0" width="16" height="320" fill="var(--gold-deep)"/>
      <rect class="gold-stripe" x="540" y="0" width="8" height="320" fill="var(--gold-deep)"/>

      <g class="brand-lockup">
        <rect x="36" y="142" width="26" height="26" fill="var(--burgundy)"/>
        <text class="brand-name" x="70" y="161" font-size="16" fill="var(--gold)">BROVENNA</text>
        <text class="brand-sub" x="36" y="188" font-size="8" fill="var(--gold)">TRADING/SHIPPING, LLC.</text>
      </g>

      <g class="contact-block" fill="var(--ink)">
        <text class="holder-name" x="262" y="112" font-size="17">Marcus T. Hollenbrand | CEO</text>

        <g class="icon-phone" transform="translate(284,150)">
          <path d="M1 1 L4 0 L6 4 L4 5.5 Q5.5 8.5 8.5 10 L10 8 L14 10 L13 13 Q5 13 1 1 Z" fill="var(--ink)"/>
        </g>
        <text class="contact-line" x="306" y="162" font-size="12">555-294-6172</text>

        <g class="icon-mail" transform="translate(284,176)">
          <rect width="14" height="11" rx="1" fill="var(--ink)"/>
          <path d="M1 1.5 L7 6.5 L13 1.5" stroke="var(--gold)" stroke-width="1.3" fill="none"/>
        </g>
        <text class="contact-line" x="306" y="187" font-size="12">mark@brovennatrading.example</text>

        <g class="icon-web" transform="translate(291,207)" fill="none" stroke="var(--ink)" stroke-width="1.3">
          <circle r="6.5"/>
          <ellipse rx="2.8" ry="6.5"/>
          <line x1="-6.5" y1="0" x2="6.5" y2="0"/>
        </g>
        <text class="contact-line" x="306" y="212" font-size="12">www.brovennatrading.example</text>
      </g>
    </svg>
  </section>

</main>
</body>
</html>
```